Website for Veteran Air Force Plumbing Combany

Project:
current site: talvikraft.com
Growing plumbing company in need of a new homepage and inner page template (2 PSDs). Their goal for their style would be to have distinct areas that direct to their main menu items (Service Areas, Services, Sewer & Drain Cleaning, Blog) (example competitor site: http://bricklanepipeworks.com/).

Homepage:

Theme: Masculine, Air Force veteran, plumbing, honest up-front pricing, free estimates

1. Style distinct areas
a. Top phone numbers with area served (High priority for customer)
i. Fort Myers: (555) 014-2876
Estero: (555) 014-2876
Naples: (555) 013-6519
Bonita Springs: (555) 013-6519
b. Social Buttons (facebook, twitter, youtube, linkedin, google+)
i. Separate Twitter Follow button
c. Logo
d. 24 HR Emergency plumber CTA button
e. Menu
f. Slider with cta buttons
g. Video spot
h. Testimonials
i. Facebook page plugin spot
j. Quick contact form (email address, small paragraph, send button)
k. Coupons
l. Page Title & Welcome paragraph
m. service columns with action buttons
n. Harlow's roster & QT Rating action buttons
o. Footer

Inner page:
1. Page title
2. Content section
3. Side bar section
a. video spot
b. Google testimonial plugin spot
c. video2 spot
d. Harlow's Roster & QT Rating action buttons

Target Market(s)

Home owners and construction managers

Industry/Entity Type

It Company

Number of Pages Required

2 page

Requirements
Must have
• Clear distinct areas for information
• Prominent area/phone number

```html
<!DOCTYPE html>
<html lang="en">
<head>
<meta charset="utf-8">
<title>Talvik Brothers Plumbing &amp; Drain</title>
<link href="https://fonts.googleapis.com/css2?family=Oswald:wght@400;500;600&family=Open+Sans:wght@400;600;700&display=swap" rel="stylesheet">
<style>
:root{
  --red:#d8312a;
  --red-dark:#b82620;
  --ink:#2b2b2b;
  --text:#555;
  --muted:#888;
  --line:#e2e2e2;
  --header:#262626;
  --footer:#2d2d2d;
  --white:#fff;
  --green-a:#1f3d2a;
  --green-b:#4f7a4a;
}
*{box-sizing:border-box;margin:0;padding:0}
html,body{width:1200px;height:2452px;overflow:hidden}
body{font-family:"Open Sans",Arial,sans-serif;color:var(--text);background:var(--white);font-size:13px;line-height:1.55;position:relative}
.heading{font-family:"Oswald","Arial Narrow",sans-serif;text-transform:uppercase;font-weight:500;letter-spacing:.5px}
.wrap{position:absolute;left:100px;width:1000px}

/* header */
.site-header{position:absolute;top:0;left:0;width:1200px;height:120px;background:linear-gradient(#333,#1c1c1c)}
.emergency-tab{position:absolute;top:0;left:480px;width:300px;height:26px;background:var(--red);color:var(--white);font-size:12px;font-weight:700;text-align:center;line-height:26px;border-radius:0 0 4px 4px}
.brand{position:absolute;left:100px;top:40px;display:flex;align-items:center;gap:12px}
.brand-mark{width:44px;height:44px;background:var(--red)}
.brand-name{font-weight:700;font-size:20px;line-height:1.15;color:var(--white);text-transform:uppercase;width:240px}
.phones{position:absolute;right:100px;top:42px;display:flex;gap:34px}
.phone{color:var(--white);font-size:11px;line-height:1.4;display:flex;gap:6px}
.phone b{display:block;font-size:12px;letter-spacing:.3px}
.phone span{color:#ccc}

/* nav */
.main-nav{position:absolute;top:120px;left:0;width:1200px;height:50px;background:var(--white);border-bottom:1px solid var(--line)}
.main-nav ul{list-style:none;display:flex;position:absolute;left:100px;top:0}
.main-nav li{font-size:12px;font-weight:600;color:var(--ink);text-transform:uppercase;padding:0 14px;line-height:50px;border-right:1px solid var(--line)}
.main-nav li:first-child{background:var(--red);color:var(--white)}
.nav-cta{position:absolute;right:100px;top:-8px;width:210px;height:62px;background:var(--red);color:var(--white);font-size:12px;font-weight:700;display:flex;align-items:center;gap:10px;padding:0 16px;line-height:1.25;text-transform:uppercase}

/* hero */
.hero{position:absolute;top:170px;left:0;width:1200px;height:450px;background:linear-gradient(160deg,#5a6470 0%,#303840 45%,#4b5560 75%,#252b31 100%)}
.hero-title{position:absolute;top:145px;left:280px;width:640px;height:48px;background:var(--red);color:var(--white);font-size:26px;line-height:48px;text-align:center}
.hero-sub{position:absolute;top:201px;left:480px;width:240px;height:34px;background:rgba(20,20,20,.85);color:var(--white);font-size:16px;line-height:34px;text-align:center}
.hero-btn{position:absolute;top:270px;left:532px;width:136px;height:40px;background:var(--red);color:var(--white);font-size:14px;line-height:40px;text-align:center;border-radius:3px}
.hero-arrow{position:absolute;top:200px}
.dots{position:absolute;bottom:14px;left:0;width:1200px;display:flex;justify-content:center;gap:6px}
.dots i{width:9px;height:9px;border-radius:50%;background:rgba(255,255,255,.5)}
.dots i:first-child{background:var(--white)}

/* trust */
.trust{top:670px;height:300px}
.trust-col{position:absolute;top:0;width:240px}
.trust h3,.testimonials h3{font-size:17px;color:var(--red);margin-bottom:10px}
.trust-row{display:flex;gap:10px;font-size:11px;line-height:1.45}
.badge{flex:0 0 96px;height:46px;background:#1d4f8c;border-radius:3px}
.badge.alt{background:#d9e3c4;border:2px solid #7a9a4b}
.testimonials{position:absolute;top:128px;left:0;width:540px}
.testimonials .quote{display:flex;gap:12px;font-size:11px;line-height:1.45}
.quote-mark{flex:0 0 40px;height:40px;background:#eee;border-radius:3px}
.activity{position:absolute;left:720px;top:0;width:280px;height:250px;border:1px solid #cfcfcf;padding:12px}
.activity h4{font-size:12px;color:var(--ink);border-bottom:1px solid var(--line);padding-bottom:6px;margin-bottom:8px}
.activity li{list-style:none;display:flex;gap:8px;font-size:10px;line-height:1.35;margin-bottom:10px;color:#3b5b98}
.activity li i{flex:0 0 26px;height:26px;background:#c8d2e4}
.activity li small{display:block;color:var(--muted)}

/* welcome */
.welcome{position:absolute;top:1110px;left:0;width:1200px;height:270px;background:linear-gradient(120deg,var(--green-a),var(--green-b) 60%,#2c4a30)}
.welcome-text{position:absolute;left:100px;top:28px;width:440px;color:#e8efe6;font-size:11px;line-height:1.5}
.welcome-text h2{font-size:20px;color:var(--white);margin-bottom:12px;font-weight:400}
.welcome-text p{margin-bottom:10px}
.video{position:absolute;left:640px;top:25px;width:460px;height:220px;background:#0f0f0f;display:flex;align-items:center;justify-content:center}

/* newsletter */
.newsletter{top:1420px}
.newsletter h2{font-size:20px;color:var(--red);font-weight:400;border-bottom:1px solid var(--line);padding-bottom:10px;margin-bottom:20px}
.form-row{display:flex;gap:18px}
.field{height:34px;border:1px solid #ccc;font-size:11px;color:var(--muted);padding:0 10px;line-height:32px}
.subscribe{width:110px;height:34px;background:var(--red);color:var(--white);font-size:12px;font-weight:700;text-align:center;line-height:34px}
.newsletter p{font-size:11px;margin-top:16px}

/* services */
.services{top:1640px;display:flex;justify-content:space-between}
.service{width:300px}
.service h3{font-size:19px;color:var(--red);font-weight:400;margin-bottom:12px}
.service-photo{width:300px;height:160px;margin-bottom:12px}
.service p{font-size:11px;line-height:1.5;margin-bottom:12px}
.btn-small{display:inline-block;background:var(--red);color:var(--white);font-size:11px;font-weight:600;padding:5px 14px;border-radius:2px}

/* checklist */
.checks{top:1950px;display:grid;grid-template-columns:repeat(3,1fr);row-gap:14px;font-size:12px;color:var(--ink);border-top:1px solid var(--line);padding-top:20px}
.checks span{display:flex;gap:8px;align-items:center}

/* footer */
.site-footer{position:absolute;top:2068px;left:0;width:1200px;height:344px;background:var(--footer);color:#bbb;font-size:11px}
.footer-col{position:absolute;top:30px}
.footer-col h4{font-size:17px;color:var(--white);font-weight:400;margin-bottom:12px}
.footer-col p{margin-bottom:10px;line-height:1.5}
.footer-col li{list-style:none;line-height:1.65}
.contact-line{display:flex;gap:8px;align-items:center;margin-bottom:8px}
.follow{display:inline-flex;gap:6px;align-items:center;background:#ddd;color:#333;font-size:10px;padding:3px 8px;border-radius:2px}
.follow i{width:10px;height:10px;background:#555}
.bottom-bar{position:absolute;top:2412px;left:0;width:1200px;height:40px;background:var(--red);color:var(--white);font-size:10px;line-height:40px}
.bottom-bar span{position:absolute}
</style>
</head>
<body>

<header class="site-header">
  <div class="emergency-tab">24 HOUR EMERGENCY PLUMBER SERVICE</div>
  <div class="brand">
    <div class="brand-mark"></div>
    <div class="brand-name">Talvik Brothers Plumbing &amp; Drain</div>
  </div>
  <div class="phones">
    <div class="phone"><svg width="10" height="14" viewBox="0 0 10 14"><path d="M5 0a5 5 0 0 1 5 5c0 4-5 9-5 9S0 9 0 5a5 5 0 0 1 5-5z" fill="#d8312a"/><circle cx="5" cy="5" r="2" fill="#262626"/></svg><div><b>FORT MYERS</b><span>(555) 014-2876</span></div></div>
    <div class="phone"><svg width="10" height="14" viewBox="0 0 10 14"><path d="M5 0a5 5 0 0 1 5 5c0 4-5 9-5 9S0 9 0 5a5 5 0 0 1 5-5z" fill="#d8312a"/><circle cx="5" cy="5" r="2" fill="#262626"/></svg><div><b>ESTERO</b><span>(555) 014-2876</span></div></div>
    <div class="phone"><svg width="10" height="14" viewBox="0 0 10 14"><path d="M5 0a5 5 0 0 1 5 5c0 4-5 9-5 9S0 9 0 5a5 5 0 0 1 5-5z" fill="#d8312a"/><circle cx="5" cy="5" r="2" fill="#262626"/></svg><div><b>NAPLES</b><span>(555) 013-6519</span></div></div>
    <div class="phone"><svg width="10" height="14" viewBox="0 0 10 14"><path d="M5 0a5 5 0 0 1 5 5c0 4-5 9-5 9S0 9 0 5a5 5 0 0 1 5-5z" fill="#d8312a"/><circle cx="5" cy="5" r="2" fill="#262626"/></svg><div><b>BONITA SPRINGS</b><span>(555) 013-6519</span></div></div>
  </div>
</header>

<nav class="main-nav">
  <ul>
    <li>Home</li><li>Service Areas</li><li>Services</li><li>Sewer &amp; Drain</li><li>Plumbing</li><li>Blog</li><li>Contact Us</li>
  </ul>
  <div class="nav-cta">
    <svg width="22" height="22" viewBox="0 0 24 24"><path d="M6.6 10.8a15 15 0 0 0 6.6 6.6l2.2-2.2c.3-.3.7-.4 1-.2 1.1.4 2.3.6 3.6.6.6 0 1 .4 1 1V20c0 .6-.4 1-1 1A17 17 0 0 1 3 4c0-.6.4-1 1-1h3.5c.6 0 1 .4 1 1 0 1.3.2 2.5.6 3.6.1.3 0 .7-.2 1z" fill="#fff"/></svg>
    <span>24 Hour Emergency<br>Plumber</span>
  </div>
</nav>

<section class="hero" role="img" aria-label="Rain on a window pane, blurred street behind">
  <svg class="hero-arrow" style="left:20px" width="20" height="36" viewBox="0 0 20 36"><path d="M18 2 2 18l16 16" stroke="#fff" stroke-width="3" fill="none"/></svg>
  <svg class="hero-arrow" style="right:20px" width="20" height="36" viewBox="0 0 20 36"><path d="m2 2 16 16L2 34" stroke="#fff" stroke-width="3" fill="none"/></svg>
  <div class="hero-title heading">Plumbing &amp; Draining Services at Your Doorstep</div>
  <div class="hero-sub heading">Lorem Ipsum is Doller</div>
  <div class="hero-btn heading">Contact Us</div>
  <div class="dots"><i></i><i></i><i></i><i></i></div>
</section>

<section class="wrap trust">
  <div class="trust-col" style="left:0">
    <h3 class="heading">QT Accredited Business</h3>
    <div class="trust-row"><div class="badge"></div><p>We are proud to hold a top QT Rating, earned through honest pricing and quality work.</p></div>
  </div>
  <div class="trust-col" style="left:290px">
    <h3 class="heading">We're Rated A on Harlow's Roster</h3>
    <div class="trust-row"><div class="badge alt"></div><p>Please review our service on Harlow's Roster and help neighbors find a plumber.</p></div>
  </div>
  <div class="testimonials">
    <h3 class="heading">Testimonials</h3>
    <div class="quote"><div class="quote-mark"></div><p>They arrived on time, quoted a fair price up front and fixed our leak the same day. Highly recommended.<br><b style="color:var(--red)">John Doe</b></p></div>
  </div>
  <aside class="activity">
    <h4>Recent Activity</h4>
    <ul>
      <li><i></i><div>Water heater flush completed<small>2 days ago</small></div></li>
      <li><i></i><div>Drain cleaning tips for winter<small>4 days ago</small></div></li>
      <li><i></i><div>New service area added in Estero<small>1 week ago</small></div></li>
      <li><i></i><div>Free estimates on repiping jobs<small>2 weeks ago</small></div></li>
    </ul>
  </aside>
</section>

<section class="welcome" role="img" aria-label="Green toned background photo of plumbing work">
  <div class="welcome-text">
    <h2 class="heading">Welcome to Talvik Brothers Plumbing &amp; Drain</h2>
    <p>We are a veteran owned plumbing company serving homeowners and builders across southwest Florida with honest, up-front pricing and free estimates on every job.</p>
    <p>From leaking faucets to full sewer line repair, our licensed team treats your home with respect and finishes the work right the first time, backed by our service guarantee.</p>
    <p>Call today and speak with a real plumber, not a call center.</p>
  </div>
  <div class="video" role="img" aria-label="Company introduction video">
    <svg width="56" height="56" viewBox="0 0 56 56"><circle cx="28" cy="28" r="26" fill="none" stroke="#fff" stroke-width="2"/><path d="M23 18v20l16-10z" fill="#fff"/></svg>
  </div>
</section>

<section class="wrap newsletter">
  <h2 class="heading">Subscribe Our Newsletter</h2>
  <div class="form-row">
    <div class="field" style="width:300px">Name</div>
    <div class="field" style="width:300px">Email</div>
    <div class="subscribe heading">Subscribe</div>
  </div>
  <p>Subscribe our newsletter for latest updates</p>
</section>

<section class="wrap services">
  <article class="service">
    <h3 class="heading">Plumbing Service Expert</h3>
    <div class="service-photo" role="img" aria-label="Plumber working on pipes under a sink" style="background:linear-gradient(135deg,#8fa9c0,#3f5f80)"></div>
    <p>Repairs, installs and upgrades for kitchens and baths, done by licensed local plumbers.</p>
    <span class="btn-small">Read More</span>
  </article>
  <article class="service">
    <h3 class="heading">Convenient Service Area</h3>
    <div class="service-photo" role="img" aria-label="Map of the service area" style="background:linear-gradient(135deg,#e8e4d6,#cfd8c0)"></div>
    <p>Serving Fort Myers, Estero, Naples and Bonita Springs with fast local response.</p>
    <span class="btn-small">Read More</span>
  </article>
  <article class="service">
    <h3 class="heading">Residential or Commercial</h3>
    <div class="service-photo" role="img" aria-label="Bright modern bathroom interior" style="background:linear-gradient(135deg,#f2f2f0,#c9ccd0)"></div>
    <p>From single homes to large job sites, we handle plumbing projects of every size.</p>
    <span class="btn-small">Read More</span>
  </article>
</section>

<section class="wrap checks">
  <span><svg width="14" height="14" viewBox="0 0 14 14"><path d="m2 7 3 3 7-7" stroke="#d8312a" stroke-width="2.4" fill="none"/></svg>Backflow Testing and Repair</span>
  <span><svg width="14" height="14" viewBox="0 0 14 14"><path d="m2 7 3 3 7-7" stroke="#d8312a" stroke-width="2.4" fill="none"/></svg>Commercial Repair and Remodel</span>
  <span><svg width="14" height="14" viewBox="0 0 14 14"><path d="m2 7 3 3 7-7" stroke="#d8312a" stroke-width="2.4" fill="none"/></svg>Hydro Drain Jetting</span>
  <span><svg width="14" height="14" viewBox="0 0 14 14"><path d="m2 7 3 3 7-7" stroke="#d8312a" stroke-width="2.4" fill="none"/></svg>Residential Repair and Remodel</span>
  <span><svg width="14" height="14" viewBox="0 0 14 14"><path d="m2 7 3 3 7-7" stroke="#d8312a" stroke-width="2.4" fill="none"/></svg>Sewer and Drain Cleaning</span>
  <span><svg width="14" height="14" viewBox="0 0 14 14"><path d="m2 7 3 3 7-7" stroke="#d8312a" stroke-width="2.4" fill="none"/></svg>Hydro Video Camera / Locating</span>
</section>

<footer class="site-footer">
  <div class="footer-col" style="left:100px;width:300px">
    <h4 class="heading">About Us</h4>
    <p>We are a veteran owned plumbing team built on discipline, honesty and hard work. Every estimate is free and every price is given before we start.</p>
    <p>Our crews are licensed, insured and trained to keep your home running, day or night.</p>
  </div>
  <div class="footer-col" style="left:480px;width:200px">
    <h4 class="heading">Quick Links</h4>
    <ul><li>Home</li><li>About Us</li><li>Service Areas</li><li>Services</li><li>Sewer &amp; Drain</li><li>Cleaning</li><li>Blog</li><li>Contact Us</li></ul>
  </div>
  <div class="footer-col" style="left:780px;width:320px">
    <h4 class="heading">Contact Us</h4>
    <p>Talvik Brothers Plumbing &amp; Drain LLC<br>4400 Harbor Line Rd, Fort Myers</p>
    <div class="contact-line"><svg width="14" height="10" viewBox="0 0 14 10"><rect x=".5" y=".5" width="13" height="9" fill="none" stroke="#bbb"/><path d="m1 1 6 5 6-5" stroke="#bbb" fill="none"/></svg>info@talvikraft.com</div>
    <div class="contact-line"><svg width="12" height="12" viewBox="0 0 24 24"><path d="M6.6 10.8a15 15 0 0 0 6.6 6.6l2.2-2.2c.3-.3.7-.4 1-.2 1.1.4 2.3.6 3.6.6.6 0 1 .4 1 1V20c0 .6-.4 1-1 1A17 17 0 0 1 3 4c0-.6.4-1 1-1h3.5c.6 0 1 .4 1 1 0 1.3.2 2.5.6 3.6.1.3 0 .7-.2 1z" fill="#bbb"/></svg>+1 (555) 019-4402</div>
    <span class="follow"><i></i>Follow</span>
  </div>
</footer>

<div class="bottom-bar">
  <span style="left:100px">Terms &amp; Condition - Privacy Policy - Sitemap</span>
  <span style="right:100px">The Talvik Brothers. Copyright All Rights Reserved</span>
</div>

</body>
</html>
```